Vorla Advise Business Cards

We need a business card design for Vorla Advise (Logo Attached), a management consultancy specialized in brand & business building.

Design should be clean, smart and a touch of innnovation without being gimmicky.

The details on the card should be:
Name: Tomas Vellaquin
Title: Managing Director
Address: 42 Marden Wharf, Kestrel Tower Building, Singapore 073296
Tel: +6284729156048
email: tv@vorlaadvise.example
website: vorlaadvise.example

For further background on corporate identity, please check www.vorlaadvise.example
Updates

Dear all,

Many thanks for the submissions so far! I gave feedback to those designs that I prefer at this stage.

Overall I see that my preference goes into the direction that 'less is more' and 'simple is beautiful'

Please create uniqueness and standout by the simplicity and attraction of the overall concept and design.

Many thanks and please shout incase of questions!

Tomas

Industry/Entity Type

Business

```html
<!DOCTYPE html>
<html lang="en">
<head>
<meta charset="utf-8">
<title>Vorla Advise Business Card Design</title>
<link rel="stylesheet" href="https://fonts.googleapis.com/css2?family=Hind:wght@400;500;600&display=swap">
<style>
  :root {
    --orange: #fb6a07;
    --ink: #4a4a4a;
    --text: #555555;
    --white: #ffffff;
    --bg-mid: #ececec;
    --bg-edge: #d6d6d6;
  }
  * { margin: 0; padding: 0; box-sizing: border-box; }
  html, body { width: 1200px; height: 1000px; overflow: hidden; }
  body {
    position: relative;
    font-family: "Hind", sans-serif;
    background: radial-gradient(ellipse at 60% 40%, var(--bg-mid) 0%, #dedede 60%, var(--bg-edge) 100%);
    color: var(--text);
  }
  .wordmark {
    font-family: "Hind", sans-serif;
    font-weight: 600;
    color: var(--ink);
    white-space: nowrap;
    line-height: 1;
  }

  /* Presentation heading */
  .presentation-title {
    position: absolute;
    right: 82px;
    top: 180px;
    text-align: right;
  }
  .presentation-title .wordmark { font-size: 66px; letter-spacing: 1px; }
  .presentation-title .subtitle {
    font-size: 22px;
    color: var(--text);
    margin-top: 6px;
    letter-spacing: 0.3px;
  }

  /* Cards */
  .card {
    position: absolute;
    left: 41px;
    width: 607px;
    height: 326px;
  }
  .card-front { top: 150px; background: var(--white); }
  .card-back { top: 510px; background: var(--orange); }

  .holder {
    position: absolute;
    left: 72px;
    top: 52px;
    text-align: right;
  }
  .holder .person-name { font-size: 21px; font-weight: 500; color: var(--ink); line-height: 1.1; }
  .holder .person-role { font-size: 11.5px; font-weight: 600; color: var(--orange); line-height: 1.2; }

  .company-block {
    position: absolute;
    left: 316px;
    top: 157px;
  }
  .company-block .wordmark { font-size: 36px; }
  .address { font-size: 13.5px; line-height: 16px; margin-top: 8px; color: var(--text); }
  .contact-list { list-style: none; margin-top: 6px; }
  .contact-list li {
    display: flex;
    align-items: center;
    font-size: 13.5px;
    height: 21px;
  }
  .contact-list svg { width: 12px; height: 12px; margin: 0 9px 0 4px; flex: none; }

  .back-logo {
    position: absolute;
    left: 119px;
    top: 128px;
  }
  .back-logo .wordmark { font-size: 56px; }
  .tagline {
    color: var(--white);
    font-size: 13px;
    font-weight: 500;
    letter-spacing: 0.2px;
    margin-left: 28px;
    margin-top: 4px;
  }
</style>
</head>
<body>
  <header class="presentation-title">
    <div class="wordmark">Vorla Advise</div>
    <p class="subtitle">Business Card Design</p>
  </header>

  <section class="card card-front" aria-label="Business card front">
    <div class="holder">
      <p class="person-name">Tomas Vellaquin</p>
      <p class="person-role">Marketing Manager</p>
    </div>
    <div class="company-block">
      <div class="wordmark">Vorla Advise</div>
      <p class="address">42 Marden Wharf, Kestrel Tower Building,<br>Singapore 073296</p>
      <ul class="contact-list">
        <li>
          <svg viewBox="0 0 12 12" aria-hidden="true"><path d="M1 3.5 Q6 0.5 11 3.5 L10 5 L8 4.5 L8 3.8 Q6 3 4 3.8 L4 4.5 L2 5 Z M2.5 6 L9.5 6 L10.5 10.5 L1.5 10.5 Z" fill="var(--orange)"/><circle cx="6" cy="8.2" r="1.2" fill="#fff"/></svg>
          +6284729156048
        </li>
        <li>
          <svg viewBox="0 0 12 12" aria-hidden="true"><rect x="0.5" y="2.5" width="11" height="7.5" fill="var(--orange)"/><path d="M0.8 2.8 L6 7 L11.2 2.8" stroke="#fff" stroke-width="1" fill="none"/></svg>
          tv@vorlaadvise.example
        </li>
        <li>
          <svg viewBox="0 0 12 12" aria-hidden="true"><rect x="0.5" y="0.5" width="11" height="11" rx="2" fill="var(--orange)"/><circle cx="6" cy="6" r="3" stroke="#fff" stroke-width="1" fill="none"/><path d="M3 6 H9 M6 3 V9" stroke="#fff" stroke-width="0.8"/></svg>
          www.vorlaadvise.example
        </li>
      </ul>
    </div>
  </section>

  <section class="card card-back" aria-label="Business card back">
    <div class="back-logo">
      <div class="wordmark">Vorla Advise</div>
      <p class="tagline">PEOPLE-FIRST STRATEGY FOR GROWING COMPANIES</p>
    </div>
  </section>
</body>
</html>
```